Rack Card Design for an Ayurvedic Beauty Product Project

Hello, I need to have rack cards. The rack cards would be about 3 products we are showcasing at an event. I am a cosmetic company. I have a logo and basic design ideas. I have attached some product images and info. By no means am I a designer so please excuse my messy AI files. Please feel free to design this as feminine as you like. :)

Target Market(s)

Beauty industry, organic, holistic, ayurveda

Industry/Entity Type

Cosmetic

```html
<!DOCTYPE html>
<html lang="en">
<head>
<meta charset="utf-8">
<title>Velvet Lotus Rack Cards</title>
<link href="https://fonts.googleapis.com/css2?family=Great+Vibes&family=Jost:wght@300;400&family=Questrial&family=Montserrat:wght@600&display=swap" rel="stylesheet">
<style>
  :root{
    --backdrop:#936b3f;
    --plum:#861f5b;
    --plum-deep:#560c38;
    --plum-light:#a03272;
    --gold:#e6bf7c;
    --gold-soft:#f6e3b8;
    --ink-light:#ffffff;
  }
  html,body{margin:0;padding:0;width:1200px;height:1145px;overflow:hidden;background:var(--backdrop);}
  .canvas{position:relative;width:1200px;height:1145px;}
  .card{position:absolute;top:106px;width:415px;height:931px;overflow:hidden;box-shadow:0 4px 14px rgba(0,0,0,.35);
        background:linear-gradient(160deg,var(--plum-light) 0%,var(--plum) 45%,var(--plum-deep) 100%);}
  .card--front{left:160px;}
  .card--products{left:625px;}
  .card-bg{position:absolute;inset:0;}
  .abs{position:absolute;}

  /* front card */
  .brand-mark{left:127px;top:52px;width:160px;height:160px;border-radius:50%;border:10px solid var(--gold);box-sizing:border-box;}
  .brand-name{left:0;right:0;top:272px;text-align:center;font-family:"Montserrat",sans-serif;font-weight:600;font-size:29px;color:var(--gold);letter-spacing:.5px;margin:0;}
  .product-line{left:0;right:0;top:311px;text-align:center;font-family:"Questrial",sans-serif;font-size:22px;line-height:27px;color:var(--ink-light);margin:0;}
  .story{left:46px;width:322px;top:540px;text-align:center;font-family:"Jost",sans-serif;font-weight:300;font-size:17.5px;line-height:22.3px;color:var(--gold);margin:0;}
  .story .drop{float:left;height:44px;font-family:"Great Vibes",cursive;font-size:60px;line-height:44px;margin:2px 6px 0 0;}

  /* product panels */
  .product-shot{border-radius:6px;}
  .shot-tube{background:linear-gradient(180deg,#8e2c68 0%,#6e1a4c 78%,#d9b675 82%,#b48a4a 100%);}
  .shot-jar{background:linear-gradient(180deg,#d7b46e 0%,#c59a52 16%,#f2f2f2 18%,#dcdcdc 100%);border-radius:10px;}
  .product-title{font-family:"Great Vibes",cursive;font-size:31px;line-height:30px;color:var(--gold);margin:0;}
  .product-copy{font-family:"Jost",sans-serif;font-weight:400;font-size:15.5px;line-height:20px;color:var(--ink-light);margin:0;}
  .panel-toner .product-title{left:150px;top:32px;}
  .panel-toner .product-copy{left:150px;top:132px;width:232px;}
  .panel-cream .product-title{left:169px;width:230px;top:352px;text-align:center;}
  .panel-cream .product-copy{left:200px;width:168px;top:448px;text-align:center;}
  .panel-serum .product-title{right:124px;top:666px;text-align:right;}
  .panel-serum .product-copy{right:124px;width:244px;top:761px;text-align:right;}
</style>
</head>
<body>
<div class="canvas">

  <section class="card card--front">
    <svg class="card-bg" width="415" height="931" viewBox="0 0 415 931" aria-hidden="true">
      <defs>
        <linearGradient id="front-lower" x1="0" y1="0" x2="1" y2="1">
          <stop offset="0" stop-color="#9e2f6f"/><stop offset="1" stop-color="#5a0d3b"/>
        </linearGradient>
      </defs>
      <path d="M0,494 Q207,368 415,500 V931 H0 Z" fill="url(#front-lower)"/>
      <path d="M0,494 Q207,368 415,500" fill="none" stroke="#f4dfb0" stroke-width="9"/>
    </svg>
    <div class="abs brand-mark"></div>
    <h1 class="abs brand-name">VELVET LOTUS</h1>
    <p class="abs product-line">Ayurvedic<br>Firming &amp; Lifting<br>Breast Cream</p>
    <p class="abs story"><span class="drop">V</span>elvet Lotus curates organic infused products where holistic skin care meets a luxurious experience. Each ingredient is carefully selected; providing Ayurvedic herbs, rich minerals &amp; elements. Stimu­lating hydration and anti-oxidants to lift, firm and illuminate your skin. We believe in connecting with your inner mantra, stimulating higher vibrations, self-esteem, positive mind and soul. As a brand we work with our experts/suppliers of Ayurveda to ensure that our products meet the quality, wholesome healing that you need.</p>
  </section>

  <section class="card card--products">
    <svg class="card-bg" width="415" height="931" viewBox="0 0 415 931" aria-hidden="true">
      <defs>
        <linearGradient id="panel-top" x1="0" y1="0" x2="1" y2="1">
          <stop offset="0" stop-color="#8c2462"/><stop offset="1" stop-color="#4f0a34"/>
        </linearGradient>
        <linearGradient id="panel-bottom" x1="0" y1="0" x2="1" y2="1">
          <stop offset="0" stop-color="#6a1447"/><stop offset="0.5" stop-color="#8f2563"/><stop offset="1" stop-color="#a23373"/>
        </linearGradient>
      </defs>
      <path d="M0,0 H415 V196 Q300,330 110,305 Q40,295 0,270 Z" fill="url(#panel-top)"/>
      <path d="M415,196 Q300,330 110,305 Q40,295 0,270" fill="none" stroke="#f4dfb0" stroke-width="8"/>
      <path d="M100,308 Q20,400 60,500 Q85,560 110,575" fill="none" stroke="#e6bf7c" stroke-width="6"/>
      <path d="M0,712 Q60,585 210,582 Q330,582 415,628 V931 H0 Z" fill="url(#panel-bottom)"/>
      <path d="M0,712 Q60,585 210,582 Q330,582 415,628" fill="none" stroke="#f4dfb0" stroke-width="8"/>
    </svg>

    <div class="panel-toner">
      <div class="abs product-shot shot-tube" style="left:33px;top:28px;width:84px;height:217px;" role="img" aria-label="Product photo: firming and lifting toner tube"></div>
      <h2 class="abs product-title">Velvet Lotus<br>Firming &amp; Lifting<br>Breast Toner</h2>
      <p class="abs product-copy">Using all natural Ayurvedic herbs, our breast toner, prepares the area for maximum absorption, giving you the best results and the most invigorating treatment</p>
    </div>

    <div class="panel-cream">
      <div class="abs product-shot shot-jar" style="left:36px;top:357px;width:134px;height:188px;" role="img" aria-label="Product photo: firming and lifting cream jar"></div>
      <h2 class="abs product-title">Velvet Lotus<br>Firming &amp; Lifting<br>Breast Cream</h2>
      <p class="abs product-copy">Using all natural Ayurvedic herbs, our breast cream helps enhance, tighten, and lift your breast</p>
    </div>

    <div class="panel-serum">
      <div class="abs product-shot shot-tube" style="left:310px;top:674px;width:62px;height:227px;" role="img" aria-label="Product photo: firming and toning serum tube"></div>
      <h2 class="abs product-title">Velvet Lotus<br>Firming and Toning<br>Breast Serum</h2>
      <p class="abs product-copy">Using all natural Ayurvedic herbs, and a touch of 24k gold, our serum enhances the experience and quality of results when part­nered with the Velvet Lotus Firming and Lifting Breast Cream provid­ing an all-dayboosting experience</p>
    </div>
  </section>

</div>
</body>
</html>
```